Modern Business Card For A Digital Advertising Company

I'll be print on the Tally Prints Velvet paper http://us.tallyprints-example.com/products/velvet/business-cards.html
Need's to be modern and use the color palette of the logo or gray scales. I think integrating the pixelation of the logo in to the card and having it wrap from one side to the other could be interesting. My company provides ad operations, web development, and number of other services to websites around the world. You can see my website at http://www.brightorbitads-example.com
Contact info on the card needs to have
Dana Welby
President
p.555.308.4127
dana@brightorbitads-example.com
http://www.brightorbitads-example.com
Doesn't necessarily need to be in that order
Target Market(s)
Website owners
Industry/Entity Type
Business
Look and feel
Each slider illustrates characteristics of the customer's brand and the style your logo design should communicate.

```html
<!DOCTYPE html>
<html lang="en">
<head>
<meta charset="utf-8">
<title>Bright Orbit Ads – Business Card</title>
<link rel="stylesheet" href="https://fonts.googleapis.com/css2?family=Tinos&display=swap">
<style>
  :root{
    --backdrop:#2b2620;
    --green-bright:#62d414;
    --green-band:#6bd81a;
    --green-soft:#93d564;
    --mist:#e6e9e3;
    --charcoal:#444546;
    --charcoal-deep:#333435;
    --ink:#1d1d1d;
    --lime-text:#c4f23c;
  }
  *{margin:0;padding:0;box-sizing:border-box}
  html,body{width:922px;height:1200px;overflow:hidden;background:var(--backdrop)}
  .canvas{position:relative;width:922px;height:1200px}
  .card{
    position:absolute;left:31px;top:350px;width:860px;height:500px;
    border-radius:14px;overflow:hidden;
    font-family:"Tinos","Times New Roman",serif;color:var(--ink);
    background:linear-gradient(160deg,var(--green-soft) 0%,#cfe6bd 55%,#eef0ec 100%);
  }
  .card-shapes{position:absolute;inset:0;width:860px;height:500px}
  .fold-area{
    position:absolute;left:430px;top:100px;width:300px;height:90px;
    background:linear-gradient(160deg,#f4f5f2,#c4c8c0);
    clip-path:polygon(0 0,100% 45%,95% 100%);
  }
  .names{position:absolute;right:30px;top:14px;text-align:right;line-height:1}
  .names .name{display:block;font-size:24px;margin-bottom:8px}
  .names .title{display:block;font-size:17px;margin-top:-4px}
  .brand{position:absolute;left:44px;top:170px;display:flex;align-items:center;gap:14px}
  .brand-mark{width:34px;height:34px;background:var(--green-bright)}
  .brand-name{font-size:40px;color:var(--charcoal-deep);letter-spacing:1px}
  .tag-pill{
    position:absolute;left:560px;top:232px;width:270px;height:44px;border-radius:22px;
    background:var(--charcoal-deep);color:var(--lime-text);
    font-size:19px;letter-spacing:.5px;display:flex;align-items:center;justify-content:center;
    text-transform:uppercase;
  }
  .contact{position:absolute;left:40px;top:372px;list-style:none}
  .contact li{display:flex;align-items:center;gap:12px;font-size:22px;height:38px}
  .contact svg{width:30px;height:30px;flex:none}
  .phone{
    position:absolute;right:22px;bottom:40px;display:flex;align-items:center;gap:10px;
    font-size:24px;color:var(--ink);
  }
  .phone svg{width:34px;height:34px}
</style>
</head>
<body>
<main class="canvas">
  <section class="card">
    <svg class="card-shapes" viewBox="0 0 860 500" aria-hidden="true">
      <path d="M400,0 H860 V160 L420,95 Z" fill="var(--charcoal)"/>
      <path d="M0,350 C260,335 560,300 860,255 V500 H0 Z" fill="var(--green-band)"/>
      <path d="M610,500 Q720,405 860,300 V500 Z" fill="#4a4b4c"/>
    </svg>
    <div class="fold-area" role="img" aria-label="Peeled paper corner decoration"></div>

    <div class="names">
      <span class="name">Dana Welby</span>
      <span class="name">Dana Welby</span>
      <span class="name">Dana Welby</span>
      <span class="title">President</span>
    </div>

    <div class="brand">
      <span class="brand-mark"></span>
      <span class="brand-name">Bright Orbit</span>
    </div>

    <div class="tag-pill">Bright Orbit Ads</div>

    <ul class="contact">
      <li>
        <svg viewBox="0 0 30 30"><path d="M3,15 L15,4 L27,15 H23 V27 H17 V19 H13 V27 H7 V15 Z" fill="#1d1d1d"/></svg>
        Your address Here
      </li>
      <li>
        <svg viewBox="0 0 30 30"><rect x="2" y="5" width="26" height="20" rx="2" fill="#1d1d1d"/><path d="M4,8 L15,17 L26,8 M4,23 L12,15 M26,23 L18,15" stroke="#ffffff" stroke-width="1.6" fill="none"/></svg>
        dana@brightorbitads-example.com
      </li>
      <li>
        <svg viewBox="0 0 30 30"><g fill="none" stroke="#1d1d1d" stroke-width="2"><circle cx="15" cy="15" r="11"/><ellipse cx="15" cy="15" rx="5" ry="11"/><path d="M4,15 H26 M6,9 H24 M6,21 H24"/></g></svg>
        www.brightorbitads-example.com
      </li>
    </ul>

    <div class="phone">
      <svg viewBox="0 0 34 34"><circle cx="17" cy="17" r="15" fill="none" stroke="#1d1d1d" stroke-width="2.2"/><path d="M11,9 L14,9 L15.5,13 L13.5,14.5 Q15,18.5 19.5,20.5 L21,18.5 L25,20 L25,23 Q24,25.5 21,25 Q11,22 9,12 Q9,9.5 11,9 Z" fill="#1d1d1d"/></svg>
      555.308.4127
    </div>
  </section>
</main>
</body>
</html>
```